Mental Health

QRT HAVEN
Behavioral Health
4172 W. Pell St. Mesa, AZ 85219
Gwendolyn (480)555-0142 / Omar 480-555-0187

Email: QRTHaven@Mailvex.example
Newly Remodeled & Spacious
g Staff
Registered Nurses
Licensed Independent &
Professional Substance &
Abuse Counselors
Behavioral Health Techs
Certified Caregivers
Behavioral Health &
Substance Abuse Professionals

To Refer a Patient
About Us
QRT Haven is a Fully Staffed Behavioral
Health Residential Facility, providing
treatment plans for adults suffering
with various Behavioral Health and
Substance Abuse disorders, while living
in a nice safe, clean and supportive
environment. Our home offers clients the
ability to learn the necessary skills to
help clients adapt, build self confidence
as well as independence, with the goal
of reducing the probability of a future
crisis or possible relapse. We offer
counseling programs, consisting of a
variety of addiction and recovery support
groups, independent living, coping and
social skills groups, as well as assisting
clients with using tools to create a resume
to help obtain employment and so much
more. We are committed to teaching
self management care and allowing
clients to understand how to utilize the
resources, skills and tools available for
long term success by providing superior
quality, all-inclusive living arrangements
and treatment options.

Thank you for your patience while I update the final content needed for us to make the final decision this week.

```html
<!DOCTYPE html>
<html lang="en">
<head>
<meta charset="utf-8">
<title>QRT Haven Business Card</title>
<link rel="stylesheet" href="https://fonts.googleapis.com/css2?family=Poppins:wght@400;500&family=Courgette&display=swap">
<style>
  :root {
    --bg: #cfd2d4;
    --card: #ffffff;
    --ink: #555a5e;
    --grey: #676a6c;
    --blue: #1f6fc0;
    --green: #7cb342;
    --orange: #f07a2a;
    --purple: #5a3a94;
    --pink: #e0559a;
    --yellow: #f3b53a;
    --red: #d6232a;
    --sky: #5b8fd6;
    --rose: #ef7fb4;
    --teal: #12a085;
  }
  * { box-sizing: border-box; margin: 0; padding: 0; }
  html, body { width: 1200px; height: 928px; overflow: hidden; }
  body {
    background: var(--bg);
    font-family: "Poppins", sans-serif;
    color: var(--ink);
    position: relative;
  }
  .card {
    position: absolute;
    left: 240px;
    width: 720px;
    height: 411px;
    background: var(--card);
    border-radius: 26px;
    box-shadow: 0 6px 18px rgba(0,0,0,.18);
    overflow: hidden;
  }
  .card--front { top: 40px; }
  .card--back { top: 477px; }

  .brand { position: absolute; display: flex; flex-direction: column; }
  .brand__row { display: flex; align-items: center; gap: 12px; }
  .brand__dot { width: 22px; height: 22px; border-radius: 50%; background: var(--green); }
  .brand__name { font-weight: 500; color: var(--blue); letter-spacing: 2px; }
  .brand__tag { color: var(--grey); letter-spacing: 3px; text-transform: uppercase; margin-top: 4px; }

  .card--front .brand { left: 60px; top: 150px; }
  .card--front .brand__name { font-size: 46px; line-height: 1; }
  .card--front .brand__tag { font-size: 19px; }

  .services { position: absolute; left: 390px; top: 88px; list-style: none; }
  .services li { font-size: 17px; line-height: 23.5px; display: flex; align-items: center; gap: 12px; color: var(--ink); }
  .services li::before { content: ""; width: 9px; height: 9px; border-radius: 50%; background: var(--c); flex: none; }

  .card--back .brand { left: 60px; top: 42px; }
  .card--back .brand__name { font-size: 36px; line-height: 1; }
  .card--back .brand__tag { font-size: 15px; }

  .contact { position: absolute; left: 60px; top: 160px; }
  .person { margin-bottom: 14px; }
  .person__name { font-family: "Courgette", cursive; font-size: 28px; line-height: 1.2; }
  .person__name--blue { color: var(--blue); }
  .person__name--green { color: var(--green); }
  .line { display: flex; align-items: center; gap: 8px; font-size: 17px; color: var(--ink); line-height: 26px; }
  .line svg { width: 16px; height: 16px; flex: none; }

  .decor {
    position: absolute;
    right: -90px;
    top: -60px;
    width: 340px;
    height: 380px;
    border-radius: 50%;
    background: radial-gradient(circle at 40% 55%, rgba(124,179,66,.55), rgba(31,111,192,.25) 55%, rgba(240,122,42,.2) 80%, rgba(255,255,255,0) 100%);
  }
</style>
</head>
<body>
  <section class="card card--front">
    <div class="brand">
      <div class="brand__row">
        <span class="brand__dot"></span>
        <span class="brand__name">QRT HAVEN</span>
      </div>
      <span class="brand__tag">Behavioral Health</span>
    </div>
    <ul class="services">
      <li style="--c: var(--blue)">Newly Remodeled</li>
      <li style="--c: var(--orange)">Spaciousg Staff</li>
      <li style="--c: var(--purple)">Registered Nurses</li>
      <li style="--c: var(--pink)">Licensed Independent</li>
      <li style="--c: var(--yellow)">Professional Substance</li>
      <li style="--c: var(--green)">Abuse Counselors</li>
      <li style="--c: var(--red)">Behavioral Health Techs</li>
      <li style="--c: var(--sky)">Certified Caregivers</li>
      <li style="--c: var(--rose)">Behavioral Health</li>
      <li style="--c: var(--teal)">Substance Abuse Professionals</li>
    </ul>
  </section>

  <section class="card card--back">
    <div class="decor" role="img" aria-label="Large brand symbol decoration area"></div>
    <div class="brand">
      <div class="brand__row">
        <span class="brand__dot"></span>
        <span class="brand__name">QRT HAVEN</span>
      </div>
      <span class="brand__tag">Behavioral Health</span>
    </div>
    <div class="contact">
      <div class="person">
        <div class="person__name person__name--blue">Gwendolyn</div>
        <div class="line">
          <svg viewBox="0 0 16 16"><path d="M4 1.5 6.5 4.5 5 6.2c.9 1.9 2.4 3.4 4.3 4.3L11 9l3 2.5-1.5 2.8C7 14 2 9 1.7 3.5z" fill="var(--red)"/></svg>
          <span>(480)555-0142</span>
        </div>
      </div>
      <div class="person">
        <div class="person__name person__name--green">Omar</div>
        <div class="line">
          <svg viewBox="0 0 16 16"><path d="M4 1.5 6.5 4.5 5 6.2c.9 1.9 2.4 3.4 4.3 4.3L11 9l3 2.5-1.5 2.8C7 14 2 9 1.7 3.5z" fill="var(--purple)"/></svg>
          <span>480-555-0187</span>
        </div>
      </div>
      <div class="line">
        <svg viewBox="0 0 16 16"><rect x="1" y="3" width="14" height="10" rx="1" fill="var(--pink)"/><path d="M1.5 3.8 8 9l6.5-5.2" stroke="#fff" stroke-width="1.3" fill="none"/></svg>
        <span>QRTHaven@Mailvex.example</span>
      </div>
      <div class="line">
        <svg viewBox="0 0 16 16"><path d="M8 15s5-5.2 5-8.8A5 5 0 0 0 3 6.2C3 9.8 8 15 8 15z" fill="var(--orange)"/><circle cx="8" cy="6.3" r="1.9" fill="#fff"/></svg>
        <span>4172 W. Pell St. Mesa, AZ 85219</span>
      </div>
    </div>
  </section>
</body>
</html>
```